Business cards, poster and standing banners for Fendrix.org needed under 48h!

Hi Genius designers,
I have a seemingly very simple project, I am organizing a open source hardware hackathon (www.fendrix.org) and need 6 deliverables:
1) a better looking png logo with transparent background (one light grey, one dark grey color. Only the middle Anarchy A have to remain red) (deadline March 18)
2) a better looking square picture (for social media identity) (deadline March 18)
3) business cards (deadline March 18) (name, email, mobile, twitter, www.fendrix.org)
4) A3 poster (deadline March 18), should include:
- Tagline: Non-profit Open Source Hardware Hardware
- Date: March 28-30
- Venue: Boltyard Lower-Valley, 912 Quillmere Rd, San Carlos
- Join the Hardware renaissance!
- www.fendrix.org
- QR code (attached)
5) standard standing banners (deadline March 20)
I attached existing logo just need it to be better, and a background picture to use for all these marketing materials. Just need someone to make all these very professional.
Attached:
- existing logo
- existing square image for social media identity
- bakcground
- QR code to include in A3 poster
Updates
Please use existing logo, i am not looking for a new logo, just need a professional version of the existing logo (anarchy A in red)
Target Market(s)
20-35 entrepreneurs, new generation of hardware engineers, makers
Industry/Entity Type
Marketing
Look and feel

```html
<!DOCTYPE html>
<html lang="en">
<head>
<meta charset="utf-8">
<title>Fendrix – Business Card</title>
<link rel="stylesheet" href="https://fonts.googleapis.com/css2?family=Arimo:wght@700&family=Roboto+Condensed:wght@400;700&display=swap">
<style>
  :root {
    --page-bg: #f3f1ec;
    --card-dark: #2e2e2e;
    --card-mid: #5f5f5f;
    --card-light: #8a8a8a;
    --band-white: #ffffff;
    --dot-grey: #c9c9c9;
    --name-grey: #c6c6c6;
    --accent-red: #c1272d;
    --title-white: #ffffff;
    --ink: #0d0d0d;
  }
  html, body {
    margin: 0;
    width: 1200px;
    height: 1000px;
    overflow: hidden;
    background: var(--page-bg);
  }
  .business-card {
    position: absolute;
    left: 150px;
    top: 236px;
    width: 900px;
    height: 528px;
    overflow: hidden;
  }
  .card-texture {
    position: absolute;
    inset: 0;
    background:
      linear-gradient(135deg, rgba(0,0,0,0) 55%, rgba(0,0,0,0.45) 100%),
      linear-gradient(90deg, var(--card-dark) 0%, var(--card-mid) 35%, var(--card-light) 52%, var(--card-mid) 70%, var(--card-dark) 100%);
  }
  .role-title {
    position: absolute;
    top: 130px;
    left: 0;
    width: 100%;
    margin: 0;
    text-align: center;
    font-family: "Arimo", Arial, sans-serif;
    font-weight: 700;
    font-size: 40px;
    letter-spacing: 0.5px;
    color: var(--title-white);
    line-height: 1;
  }
  .title-rule {
    position: absolute;
    top: 188px;
    left: 135px;
    width: 672px;
    height: 3px;
    background: linear-gradient(90deg, rgba(255,255,255,0), rgba(255,255,255,0.95) 50%, rgba(255,255,255,0));
  }
  .brand-band {
    position: absolute;
    top: 221px;
    left: 0;
    width: 100%;
    height: 169px;
    background: var(--band-white);
  }
  .band-dots {
    position: absolute;
    inset: 0;
  }
  .band-dots circle { fill: var(--dot-grey); }
  .brand-name {
    position: absolute;
    top: 56px;
    left: 0;
    width: 100%;
    display: flex;
    justify-content: center;
    align-items: center;
    gap: 16px;
  }
  .brand-mark {
    width: 42px;
    height: 42px;
    border-radius: 50%;
    background: var(--accent-red);
  }
  .brand-word {
    font-family: "Arimo", Arial, sans-serif;
    font-weight: 700;
    font-size: 64px;
    line-height: 1;
    letter-spacing: 6px;
    text-transform: uppercase;
    color: var(--name-grey);
  }
  .contact-row {
    position: absolute;
    top: 400px;
    left: 0;
    width: 100%;
    display: flex;
    justify-content: center;
    gap: 34px;
    font-family: "Roboto Condensed", Arial Narrow, sans-serif;
    font-size: 22px;
    color: var(--ink);
  }
  .website {
    position: absolute;
    top: 438px;
    left: 0;
    width: 100%;
    text-align: center;
    font-family: "Roboto Condensed", Arial Narrow, sans-serif;
    font-weight: 700;
    font-size: 30px;
    color: var(--ink);
  }
</style>
</head>
<body>
  <div class="business-card">
    <div class="card-texture" role="img" aria-label="Grey low-poly triangle pattern background"></div>

    <h1 class="role-title">PROJECT OWNER</h1>
    <div class="title-rule"></div>

    <div class="brand-band">
      <svg class="band-dots" width="900" height="169" viewBox="0 0 900 169" aria-hidden="true">
        <circle cx="225" cy="18" r="6"/>
        <circle cx="316" cy="18" r="6"/>
        <circle cx="407" cy="18" r="6"/>
        <circle cx="499" cy="18" r="6"/>
        <circle cx="590" cy="18" r="6"/>
        <circle cx="681" cy="18" r="6"/>
        <circle cx="316" cy="151" r="6"/>
        <circle cx="407" cy="151" r="6"/>
        <circle cx="499" cy="151" r="6"/>
        <circle cx="590" cy="151" r="6"/>
      </svg>
      <div class="brand-name">
        <span class="brand-mark"></span>
        <span class="brand-word">Fendrix</span>
      </div>
    </div>

    <div class="contact-row">
      <span class="contact-phone">P: 123-456-789</span>
      <span class="contact-email">E: projectowner@fendrixmail.org</span>
      <span class="contact-social">T: projectowner/</span>
    </div>
    <div class="website">www.fendrix.org</div>
  </div>
</body>
</html>
```